London's best branded & leading residential inventory company requires sales pack design

Good Afternoon,

We are looking for design and print company to start working with. We have a couple of initial projects and will definitely have other projects in the future that we would require help with.

Below I have outlined the current projects that we need help with.

Silver Heron – www.silver-heron.co.uk

SALES PACKS – We have our business development manager out in the field who is visiting current and new clients. We want to stand out and be different so are open to suggestions and ways of presenting ourselves and being front of mind. Our ideas about what we want are below, we do not want the pack to be heavy with tonnes of information.

We want to create one for the professional marketing leading brand we have. We would like the pack to be small and inter changeable.

Below are the values of the company which need to be communicated through USP’s/quotes as well as the design of the pack itself.
SH VALUES
• Professional
• Solution Driven
• Trusted Partner
• Consistent
• Progressive
• Personable
PB VALUES
• Quality
• Trusted Partner
• Solution Driven
• Progressive
• Energetic
• Personable

Below is the layout we would like to give you some clear guidance as to what to produce.

Design an A5 folder – landscape, which has the 3 cards in. Below is exactly the content required and the

Every card and side should have Silver Heron logo and strap line, Tel – 020 7946 0583 Email – bookings@silver-heron.co.uk, QRTB & NLVS Accreditation

CARD 1 – Front (use branding any photos use subtly)
CUSTOMER FOCUS
- Open 7 days a week – 364 Days a year
- Inspections from 8am to 8pm
- 50 clerks during peak periods
- Dedicated bookings managers for every client

CARD 2 - Front (use branding any photos use subtly)
REPORT GUARANTEE & QUALITY
- 100% guarantee all reports back within 48 hours
- Reports created accurately and consistently using bespoke app ‘OurNest’
- 19 point quality check from proof readers for every report
- All clerks receive monthly site inspection from Head of Training

CARD 3 – Front (use branding any photos use subtly)
WHY SILVER HERON – Use photo Dorian Pell with below quote
“At Silver Heron we are dedicated to service, with the office support team open 7 days a week we can guarantee detailed management of the inspections 364 days a year (we do close for xmas!). Let us provide you with a great service by calling or emailing our team of dedicated Booking Managers for any needs or requirements”
The have the following bullet points below
- Over 45,000 inspections Carried out to the highest professional standards
- Trusted partner to 145 agents, including the most respected estate agents in London
- We know the value of a home, so we donate 5% of our profits in support of Hearthway - the UK's leading charity for homeless young people. (also have their logo in same colour as text - see front page of one of our reports that we have also now uploaded)

CARD 1 – BACK - TESTIMONIALS – Use the photos, logo and quotes.
Brambles
Tolworth Grey

CARD 2 – BACK - TESTIMONIALS – Use the photos, logo and quotes.
Quill & Barrows
Corvin Adley

CARD 3 – BACK - BACK - TESTIMONIALS – Use the photos, logo and quotes.
Mark T Hale
Meadowlarks

FRONT COVER OF FOLDER
SILVER HERON – INVENTORY REPORTS FOR LETTING AGENTS – (Use Logo & Strap line)

BACK COVER
SOARING PAST THE CROWD (The strap line)

INSIDE FRONT COVER – Use photo image of SH in the field

INSIDE BACK COVER – Use photo image of SH in the field (this section we must be able to slot the 3 cards)

CARD 4 NEW ADDITION
This needs to be a card can be perforated and divided into 4 (as per business cards), this idea being this card will be split and handed round to various people in our clients offices
So front of each card will have photo of bookings manager (use Dorian Pell for now), their name and role, must have our logo and strap line and contact details, with the words 'YOUR DEDICATED BOOKINGS MANAGER'
The BACK of each section (4 sections as to back of business card) to have our selling points, as per our reports front cover (see new upload) - must have logo and contact details as well (phone no and email)
- Open 7 days a week, 364 days a year
- Office open from 8.45am to 6.30pm
- Guaranteed 48 hour return of reports
- Over 45,000 inspections completed
- Up to 50 clerks in peak times

Target Market(s)

Estate Agents

Industry/Entity Type

It Company

Font styles to use
Other font styles liked:
• Those outlined in Brand Principles

Requirements
Nice to have
• Photos of Bookings Managers themselves - only Dorian Pell on website is current

```html
<!DOCTYPE html>
<html lang="en">
<head>
<meta charset="utf-8">
<title>Silver Heron – Folder Spread</title>
<link rel="stylesheet" href="https://fonts.googleapis.com/css2?family=Roboto+Condensed:ital,wght@0,700;1,700&family=Open+Sans:ital,wght@0,400;0,600;1,400&display=swap">
<style>
  :root {
    --purple: #3a2596;
    --purple-deep: #241766;
    --green: #0bab4f;
    --ink: #1c1c22;
    --paper: #f4f4f4;
    --stage: #e4e4e4;
    --white: #ffffff;
  }
  * { box-sizing: border-box; margin: 0; padding: 0; }
  html, body { width: 1200px; height: 1200px; overflow: hidden; }
  body { background: var(--stage); font-family: "Open Sans", sans-serif; position: relative; }

  .spread {
    position: absolute; left: 60px; top: 220px;
    width: 1080px; height: 760px;
    display: flex;
    box-shadow: 0 20px 40px rgba(0,0,0,.18);
  }
  .panel { position: relative; width: 540px; height: 760px; background: var(--paper); overflow: hidden; }
  .panel-bg { position: absolute; inset: 0; width: 100%; height: 100%; }

  /* Back cover */
  .call {
    position: absolute; top: 92px; left: 0; width: 100%; text-align: center;
    font-family: "Roboto Condensed", sans-serif; font-style: italic; font-weight: 700;
    font-size: 40px; color: var(--white); letter-spacing: .5px;
  }
  .call-label { color: var(--green); }
  .web {
    position: absolute; top: 150px; left: 0; width: 100%; text-align: center;
    color: var(--white); font-size: 14px; letter-spacing: 4px;
  }
  .detail { position: absolute; left: 60px; top: 330px; width: 400px; color: var(--ink); }
  .detail-title {
    font-family: "Roboto Condensed", sans-serif; font-style: italic; font-weight: 700;
    color: var(--green); font-size: 26px; margin-bottom: 18px;
  }
  .detail p { font-size: 13.5px; line-height: 1.45; margin-bottom: 16px; text-align: justify; }

  /* Front cover */
  .brand { position: absolute; top: 70px; right: 48px; text-align: left; }
  .brand-row { display: flex; align-items: center; gap: 12px; }
  .brand-mark { width: 14px; height: 14px; background: var(--ink); }
  .brand-name {
    font-family: "Roboto Condensed", sans-serif; font-weight: 700;
    font-size: 46px; color: var(--ink); letter-spacing: 1px; line-height: 1;
  }
  .brand-strap {
    font-family: "Open Sans", sans-serif; font-weight: 600; font-size: 10px; letter-spacing: 2.4px;
    color: var(--ink); margin-top: 8px; text-align: right;
  }
  .photo {
    position: absolute; left: 56px; top: 190px; width: 484px; height: 270px;
    background: linear-gradient(100deg, #b9a68a 0%, #d9cdb8 30%, #a9c7d4 55%, #e8e2d6 75%, #c4ad8a 100%);
  }
  .photo-rule { position: absolute; left: 40px; width: 500px; height: 4px; background: var(--green); }
  .headline {
    position: absolute; left: 56px; top: 520px; width: 470px;
    font-family: "Roboto Condensed", sans-serif; font-weight: 700; line-height: 1.05;
    white-space: nowrap;
  }
  .headline-main { display: block; font-size: 40px; color: var(--ink); }
  .headline-sub { display: block; font-size: 27px; color: var(--purple); margin-top: 4px; }
</style>
</head>
<body>
<main class="spread">

  <section class="panel back-cover">
    <svg class="panel-bg" viewBox="0 0 540 760" preserveAspectRatio="none" aria-hidden="true">
      <path d="M0 0 H540 V240 Q300 215 0 170 Z" fill="var(--purple)"/>
      <path d="M0 170 Q300 215 540 240 V262 Q300 236 0 196 Z" fill="var(--green)"/>
      <path d="M0 650 Q260 700 540 712 V760 H0 Z" fill="var(--purple-deep)"/>
      <path d="M420 760 L540 470 V760 Z" fill="var(--green)"/>
    </svg>
    <div class="call"><span class="call-label">CALL US</span> 020 7946 0583</div>
    <div class="web">www.silver-heron.co.uk</div>
    <div class="detail">
      <h2 class="detail-title">AN EYE FOR DETAIL</h2>
      <p>We're passionate about finding new and improved ways to offer our customers more. It's ingrained in the way we think and act, which is why we have invested in the best technology, guaranteed our 48 hour turnaround, and why our clerks and office team interact in the most personable manner.</p>
      <p>Simple to follow, but detailed inventory reports, compiled by friendly and well trained inventory clerks. Helpful and efficient head office support team.</p>
    </div>
  </section>

  <section class="panel front-cover">
    <svg class="panel-bg" viewBox="0 0 540 760" preserveAspectRatio="none" aria-hidden="true">
      <path d="M0 0 H120 L0 560 Z" fill="var(--green)"/>
      <path d="M0 700 Q260 722 540 716 V736 Q260 742 0 716 Z" fill="var(--purple-deep)"/>
      <path d="M0 716 Q260 742 540 736 V760 H0 Z" fill="var(--green)"/>
    </svg>
    <div class="brand">
      <div class="brand-row">
        <span class="brand-mark" aria-hidden="true"></span>
        <span class="brand-name">SILVER HERON</span>
      </div>
      <div class="brand-strap">INVENTORY REPORTS FOR LETTING AGENTS</div>
    </div>
    <div class="photo-rule" style="top:178px"></div>
    <div class="photo" role="img" aria-label="Inventory clerk with a tablet checking folded linen in a bedroom"></div>
    <div class="photo-rule" style="top:470px"></div>
    <h1 class="headline">
      <span class="headline-main">SOARING PAST THE CROWD</span>
      <span class="headline-sub">COMMITED TO GOING THE EXTRA MILE</span>
    </h1>
  </section>

</main>
</body>
</html>
```